Flyer for Harbourline Accounting & Taxation, a local tax practice

Flyer for my business to be distributed locally in the Western Suburb of Melbourne (Size: DL, Fold: Flat, Backside: Blank) This will include below information (Font, color and capitalization of the text is for the designer's creativity):
Harbourline Accounting & Taxation Your Local Tax Accountant
ABN: 37 481 259 604
Address: 9 Marlo Place, Wattle Bend
kolvend@hbatx.com.au
Call Tobias on 0419 786 205 to book your appointment
Services we offer:
Individual & Company Tax Returns
Company & Trust formation
Business Advisory
Bookkeeping
BAS & IAS
Payroll
TPAR
Please include the logo of the business attached which was designed by PixelForum few years ago.
Please include the NBF, RCQ and Lumo logos somewhere in the bottom, preferable the same size and aligned (attached)

```html
<!DOCTYPE html>
<html lang="en">
<head>
<meta charset="utf-8">
<title>Harbourline Accounting &amp; Taxation – DL Flyer</title>
<link rel="stylesheet" href="https://fonts.googleapis.com/css2?family=Jost:wght@300;400;500;600;700;800&display=swap">
<style>
  :root {
    --orange: #e8743a;
    --charcoal: #414042;
    --footer: #4a4a4c;
    --stage: #6b6b6b;
    --white: #ffffff;
    --partner-blue: #1ab4e8;
    --badge-green: #8cc63f;
    --accent-purple: #7b4fa0;
  }
  * { box-sizing: border-box; margin: 0; padding: 0; }
  html, body { width: 1200px; height: 2270px; overflow: hidden; }
  body { background: var(--stage); font-family: "Jost", sans-serif; color: var(--charcoal); position: relative; }

  .flyer {
    position: absolute; left: 123px; top: 99px; width: 954px; height: 2025px;
    background: var(--white); overflow: hidden;
    box-shadow: 6px 8px 14px rgba(0,0,0,.35);
  }
  .hero-art { position: absolute; left: 0; top: 0; width: 954px; height: 1030px; }

  .brand { position: absolute; left: 66px; top: 60px; display: flex; align-items: center; gap: 24px; }
  .brand-mark { width: 114px; height: 114px; background: var(--orange); }
  .brand-name { font-weight: 500; color: var(--charcoal); line-height: 1; }
  .brand-name .primary { display: block; font-size: 60px; letter-spacing: .5px; }
  .brand-name .secondary { display: block; font-size: 34px; margin-top: 8px; }

  .headline {
    position: absolute; left: 0; width: 100%; top: 968px; text-align: center;
    color: var(--orange); font-weight: 800; font-size: 56px; line-height: 68px; letter-spacing: -.5px;
  }
  .tagline {
    position: absolute; left: 0; width: 100%; top: 1118px; text-align: center;
    font-weight: 700; font-size: 41px; letter-spacing: -.3px; color: var(--charcoal);
  }

  .services {
    position: absolute; left: 84px; top: 1236px; width: 786px; height: 308px;
    border: 2px solid var(--charcoal); border-radius: 40px;
  }
  .services-title {
    position: absolute; left: 50%; top: -30px; transform: translateX(-50%);
    background: var(--white); padding: 0 22px; white-space: nowrap;
    color: var(--orange); font-weight: 600; font-size: 42px; line-height: 56px;
  }
  .service { position: absolute; font-size: 35px; line-height: 41px; font-weight: 400; color: var(--charcoal); }
  .service::before {
    content: ""; position: absolute; left: -37px; top: 10px; width: 20px; height: 20px; border-radius: 50%;
    background: radial-gradient(circle, #b04a1c 0 3px, var(--orange) 4px);
  }

  .accreditations { position: absolute; left: 0; top: 1585px; width: 100%; height: 100px; }
  .accreditations .divider { position: absolute; top: 0; width: 1px; height: 100px; background: #cfcfcf; }
  .accreditation { position: absolute; top: 50%; transform: translate(-50%, -50%); display: flex; align-items: center; gap: 12px; }
  .accreditation .dot { width: 74px; height: 74px; border-radius: 50%; }
  .accreditation .name { font-size: 36px; font-weight: 500; color: var(--charcoal); }
  .accreditation .small { font-size: 11px; line-height: 13px; color: var(--charcoal); }

  .booking { position: absolute; left: 0; width: 100%; top: 1728px; text-align: center; font-size: 40px; font-weight: 400; color: var(--charcoal); }

  .footer { position: absolute; left: 0; top: 1853px; width: 100%; height: 172px; background: var(--footer); }
  .rule { position: absolute; left: 0; top: 1836px; width: 100%; height: 3px; background: var(--orange); }
  .call-bar {
    position: absolute; left: 159px; top: 1795px; width: 674px; height: 84px; border-radius: 42px;
    background: var(--orange); color: var(--white);
    display: flex; align-items: center; padding-left: 56px; font-size: 48px; white-space: nowrap;
  }
  .call-bar .lead { font-weight: 300; }
  .call-bar .number { font-weight: 700; margin-left: 12px; }
  .call-icon { position: absolute; left: 107px; top: 1793px; width: 90px; height: 90px; }

  .contact { position: absolute; color: var(--white); font-size: 34px; font-weight: 300; line-height: 42px; white-space: nowrap; }
  .contact svg { vertical-align: middle; }
</style>
</head>
<body>
  <main class="flyer">
    <svg class="hero-art" viewBox="0 0 954 1030" aria-hidden="false">
      <defs>
        <linearGradient id="office-tones" x1="0" y1="0" x2="0" y2="1">
          <stop offset="0.18" stop-color="#ffffff"/>
          <stop offset="0.38" stop-color="#dde2e6"/>
          <stop offset="0.62" stop-color="#8a93a0"/>
          <stop offset="0.82" stop-color="#59606c"/>
          <stop offset="1" stop-color="#c8ccd0"/>
        </linearGradient>
        <linearGradient id="desk-tones" x1="0" y1="0" x2="1" y2="1">
          <stop offset="0" stop-color="#e7e2dc"/>
          <stop offset="1" stop-color="#c79a76"/>
        </linearGradient>
      </defs>
      <path d="M0,0 H954 V700 Q323,1007 0,809 Z" fill="var(--charcoal)"/>
      <path d="M0,0 H954 V668 Q323,986 0,769 Z" fill="var(--orange)"/>
      <path d="M0,0 H954 V630 Q323,963 0,716 Z" fill="url(#office-tones)" role="img" aria-label="Photo: two accountants in suits reviewing a chart on a laptop in an office"/>
      <circle cx="753" cy="769" r="135" fill="url(#desk-tones)" stroke="var(--orange)" stroke-width="5" role="img" aria-label="Photo: hands using a calculator and pen over paperwork"/>
    </svg>

    <div class="brand">
      <div class="brand-mark"></div>
      <div class="brand-name">
        <span class="primary">Harbourline</span>
        <span class="secondary">Accounting &amp; Taxation</span>
      </div>
    </div>

    <h1 class="headline">HARBOURLINE ACCOUNTING<br>&amp; TAXATION</h1>
    <p class="tagline">YOUR LOCAL TAX ACCOUNTANT</p>

    <section class="services">
      <h2 class="services-title">Services we offer</h2>
      <div class="service" style="left:81px; top:45px;">Individual &amp;<br>Company Tax Returns</div>
      <div class="service" style="left:81px; top:136px;">Company &amp; Trust<br>formation</div>
      <div class="service" style="left:81px; top:230px;">Business Advisory</div>
      <div class="service" style="left:528px; top:45px;">Bookkeeping</div>
      <div class="service" style="left:528px; top:95px;">BAS &amp; IAS</div>
      <div class="service" style="left:528px; top:147px;">Payroll</div>
      <div class="service" style="left:528px; top:199px;">TPAR</div>
    </section>

    <div class="accreditations">
      <div class="accreditation" style="left:259px;">
        <span class="dot" style="background:var(--partner-blue);"></span>
        <span class="name">Lumo</span>
      </div>
      <span class="divider" style="left:381px;"></span>
      <div class="accreditation" style="left:497px;">
        <span class="dot" style="background:var(--accent-purple);"></span>
        <span class="name">NBF</span>
      </div>
      <span class="divider" style="left:613px;"></span>
      <div class="accreditation" style="left:714px;">
        <span class="dot" style="background:var(--badge-green); border:4px solid #d9d9d9; width:84px; height:84px;"></span>
        <span class="small">Tax Agent<br>41870352</span>
      </div>
    </div>

    <p class="booking">to book your appointment</p>

    <div class="footer"></div>
    <div class="rule"></div>
    <div class="call-bar"><span class="lead">Call Tobias</span><span class="number">0419 786 205</span></div>
    <svg class="call-icon" viewBox="0 0 90 90" aria-label="Phone">
      <circle cx="45" cy="45" r="42" fill="var(--white)" stroke="var(--charcoal)" stroke-width="5"/>
      <path d="M31 26 l8 -3 l6 12 l-5 4 q4 9 12 13 l4 -5 l12 6 l-3 8 q-3 4 -9 3 q-17 -5 -27 -25 q-2 -8 2 -13 z" fill="var(--charcoal)"/>
      <path d="M50 26 q12 2 15 14 M50 17 q20 3 24 23" fill="none" stroke="var(--charcoal)" stroke-width="3.5" stroke-linecap="round"/>
    </svg>

    <p class="contact" style="left:57px; top:1906px;">ABN: 37 481 259 604</p>
    <p class="contact" style="left:57px; top:1951px;">
      <svg width="30" height="20" viewBox="0 0 30 20" aria-hidden="true"><rect width="30" height="20" fill="var(--orange)"/><path d="M0 0 L15 11 L30 0" fill="none" stroke="var(--footer)" stroke-width="2"/></svg>
      kolvend@hbatx.com.au
    </p>
    <svg style="position:absolute; left:578px; top:1912px;" width="24" height="32" viewBox="0 0 24 32" aria-label="Location">
      <path d="M12 0 C5 0 0 5 0 12 C0 20 12 32 12 32 C12 32 24 20 24 12 C24 5 19 0 12 0 Z" fill="var(--orange)"/>
      <circle cx="12" cy="12" r="4.5" fill="var(--footer)"/>
    </svg>
    <p class="contact" style="left:614px; top:1908px;">9 Marlo Place,<br>Wattle Bend</p>
  </main>
</body>
</html>
```